Velto Kin needs some awesome stationary

Do you have what it takes to get my brand? You either do or you don't, have a crack at a design and you my just win my business.

I don't want to waste your or my time, so put your creative genius on either a business card or envelope.

I however need a package of stationary that follows the same brand. I will message you to complete the remaining should I like your first submission.

Here is what I need, have a go!

Basically I need the following for my small business based in melbourne.
- Letterhead (printer ready and MS Word)
- Business Card
- Compliments Slip
- Envelope
- Proposal Cover Page (MS Word only)
- Presentation Folder
- Planning Poker Cards
- Student Name Tent
- Index Cards
- Dabble-Tab

I am establishing the brand and it must be modern, professional but also relaxed; that is not formal and not corporate. It represents a company are leaders, but small enough to care and operate like a bunch of friends. We are bringing people and conversations back to business, and turfing out all the bureaucracy and crazy and wasteful procedures. Its about "lets talk and figure it out together and find even better ways".

Target Market(s)

Mainly companies that build software products, but Agile practices are used in many other industries (even graphic design projects)

Industry/Entity Type

Information Technology

Font styles to use
Sans Serif

Colors
3176b5
aaaaaa

Requirements
Must have
• I like curves and circles and not boxes or rectangles.
• I want a colour rich design with my brand colours, but it must be balanced.
• I want more modern than traditional, but simple modern
Should not have
• Not corporate
• Please don't waste my time if your not going to think about it.
• Don't mess with my primary logo
• Don't change my colours
• Don't overlay logo on image

```html
<!DOCTYPE html>
<html lang="en">
<head>
<meta charset="utf-8">
<title>Velto Kin – Business Card</title>
<link href="https://fonts.googleapis.com/css2?family=Open+Sans:wght@400;600;700&display=swap" rel="stylesheet">
<style>
  :root {
    --brand-blue: #2d5ba3;
    --brand-blue-deep: #244d8f;
    --brand-blue-light: #3a6cb8;
    --brand-grey: #a3a6ab;
    --card-white: #efeff0;
    --ink: #2b2b2b;
    --backdrop: #e9e9ea;
  }
  * { box-sizing: border-box; margin: 0; padding: 0; }
  html, body { width: 1200px; height: 800px; overflow: hidden; }
  body {
    background: var(--backdrop);
    font-family: "Open Sans", Arial, sans-serif;
    display: flex;
    align-items: center;
    justify-content: center;
    gap: 110px;
  }
  .card {
    position: relative;
    width: 432px;
    height: 282px;
    overflow: hidden;
  }

  /* Front */
  .card-front { background: var(--card-white); }
  .front-brand {
    position: absolute;
    left: 26px;
    top: 120px;
    display: flex;
    align-items: center;
    gap: 10px;
  }
  .brand-dot {
    width: 22px; height: 22px;
    border-radius: 50%;
    background: var(--brand-blue);
  }
  .brand-name {
    font-size: 30px;
    font-weight: 600;
    color: var(--brand-blue);
    letter-spacing: 0.2px;
  }
  .contact-block {
    position: absolute;
    left: 210px;
    top: 34px;
  }
  .person-name {
    font-size: 17px;
    font-weight: 400;
    color: var(--brand-blue);
  }
  .person-title {
    font-size: 9px;
    color: var(--ink);
    margin-top: 5px;
  }
  .contact-list {
    list-style: none;
    margin-top: 24px;
  }
  .contact-item {
    display: flex;
    align-items: flex-start;
    gap: 9px;
    font-size: 12px;
    line-height: 17px;
    color: var(--ink);
  }
  .contact-icon {
    flex: none;
    width: 10px; height: 10px;
    margin-top: 4px;
    fill: var(--brand-blue);
  }
  .footer-band {
    position: absolute;
    left: 0; right: 0; bottom: 0;
    height: 40px;
    background: var(--brand-blue);
    color: #fff;
    font-size: 11.5px;
    display: flex;
    align-items: center;
    justify-content: center;
    gap: 6px;
  }
  .footer-phone { font-weight: 700; display: inline-flex; align-items: center; gap: 3px; }
  .footer-phone svg { width: 10px; height: 10px; fill: #fff; }

  /* Back */
  .card-back { background: var(--brand-blue); }
  .back-texture {
    position: absolute; inset: 0;
    background: radial-gradient(circle at 50% 50%, var(--brand-blue-light) 0%, var(--brand-blue) 45%, var(--brand-blue-deep) 100%);
  }
  .back-content {
    position: absolute; inset: 0;
    display: flex;
    flex-direction: column;
    align-items: center;
    justify-content: center;
    padding-bottom: 4px;
  }
  .back-brand { display: flex; align-items: center; gap: 10px; }
  .back-brand .brand-dot { background: #fff; width: 20px; height: 20px; }
  .back-brand .brand-name { color: #fff; font-size: 32px; }
  .back-url {
    margin-top: 12px;
    color: #fff;
    font-size: 13.5px;
    letter-spacing: 0.3px;
  }
</style>
</head>
<body>

  <section class="card card-front">
    <div class="front-brand">
      <span class="brand-dot"></span>
      <span class="brand-name">Velto Kin</span>
    </div>

    <div class="contact-block">
      <h1 class="person-name">Dorian Falke</h1>
      <p class="person-title">CEO, Professional Scrum Trainer</p>
      <ul class="contact-list">
        <li class="contact-item">
          <svg class="contact-icon" viewBox="0 0 10 10"><path d="M5 0a3.5 3.5 0 0 0-3.5 3.5C1.5 6 5 10 5 10s3.5-4 3.5-6.5A3.5 3.5 0 0 0 5 0zm0 5a1.4 1.4 0 1 1 0-2.8A1.4 1.4 0 0 1 5 5z"/></svg>
          <span>PO Box 4418, Harlow Creek,<br>VIC 3190, Australia</span>
        </li>
        <li class="contact-item">
          <svg class="contact-icon" viewBox="0 0 10 10"><path d="M0 2h10v6H0z" fill="none" stroke="#2d5ba3" stroke-width="1"/><path d="M0 2l5 3.5L10 2" fill="none" stroke="#2d5ba3" stroke-width="1"/></svg>
          <span>dorian@veltokin.com.au</span>
        </li>
        <li class="contact-item">
          <svg class="contact-icon" viewBox="0 0 10 10"><path d="M2 0l2 2.5-1.2 1.3a6 6 0 0 0 3.4 3.4L7.5 6 10 8l-1.5 2C4 10 0 6 0 1.5z"/></svg>
          <span>+61 400 172 583</span>
        </li>
      </ul>
    </div>

    <footer class="footer-band">
      <span>Velto Kin Pty Ltd</span>
      <span class="footer-phone"><svg viewBox="0 0 10 10"><path d="M2 0l2 2.5-1.2 1.3a6 6 0 0 0 3.4 3.4L7.5 6 10 8l-1.5 2C4 10 0 6 0 1.5z"/></svg>1300VELTO</span>
      <span>|</span>
      <span>www.veltokin.com.au</span>
    </footer>
  </section>

  <section class="card card-back">
    <div class="back-texture" role="img" aria-label="Radiating dotted texture in brand blue"></div>
    <div class="back-content">
      <div class="back-brand">
        <span class="brand-dot"></span>
        <span class="brand-name">Velto Kin</span>
      </div>
      <p class="back-url">www.veltokin.com.au</p>
    </div>
  </section>

</body>
</html>
```